Door Hanger Design for Electricians Serving Homes

I would like our logo incorporated into the door hanger. We would like a place for a tear off section on the bottom of the hanger with our contact information: K&T Electric - (555) 318-4702 - www.kandtelectric.example - info@kandtelectric.example.
Door Hanger Script
Front Side of the Door Hanger:
[Company Logo]
Need a Reliable Electrician?
Your Local Electrical Expert is Just Around the Corner!
• Quick Response Times
• Affordable Rates
• Quality Workmanship
• Fully Licensed & Insured
• Special Offer:
• 10% OFF Your First Service Call!
Back Side of the Door Hanger:
Don't Let Electrical Issues Keep You in the Dark!
From flickering lights to complete system upgrades, we've got all your
residential electrical needs covered. Our services include:
• Electrical Repairs & Troubleshooting
• Lighting Installation & Upgrades
• Safety Inspections & Code Compliance
• Energy-Efficient Solutions
• 24/7 Emergency Services
• Why Choose Us?
• Friendly, Local Service
• Over 30 Years of Experience
• Satisfaction Guaranteed
• Upfront Pricing
Call Us Today: [Your Phone Number]
Visit Our Website: [Your Website]
Book Your Appointment Now and Claim Your 10% Discount!
Offer valid for new customers on the first visit only. Mention this door hanger when
booking.
[Your Company Name and Contact Information]
Follow Us on Social Media for More Tips and Special Offers!
[Icons for social media platforms: Chatterpage, Pixmosaic, Quibbler, etc.]
Design Tips:
Use bold, clear fonts for easy reading.
Incorporate your brand colors and logo for instant recognition.
Include a clear call to action (CTA) on both sides.
Add a tear-off section at the bottom with your contact information for
convenience.
Use high-quality images or graphics related to electrical work to catch
the eye.
This door hanger design and copy aim to attract residential clients by
highlighting the benefits of your electrical services, special offers, and
how they can easily get in touch with you for their electrical needs.
The door knocker template will have three of the same design on front and three of the same design on the back. This template is from the print shop.

```html
<!DOCTYPE html>
<html lang="en">
<head>
<meta charset="utf-8">
<title>K&amp;T Electric Door Hanger</title>
<link href="https://fonts.googleapis.com/css2?family=Montserrat:wght@300;400;700;900&family=Roboto+Condensed:ital,wght@0,400;0,700;1,400&display=swap" rel="stylesheet">
<style>
:root{
  --red:#ee1c1c;
  --red-deep:#c40d0d;
  --ink:#111111;
  --charcoal:#333333;
  --steel:#9a9ca3;
  --page:#e3e3e3;
  --white:#ffffff;
  --text:#1b1b1b;
}
*{margin:0;padding:0;box-sizing:border-box}
html,body{width:1200px;height:1200px;overflow:hidden;background:var(--page)}
body{position:relative;font-family:"Roboto Condensed",sans-serif;color:var(--text)}
.hanger{position:absolute;top:73px;width:459px;height:1054px;background:var(--white);overflow:hidden;box-shadow:0 14px 28px rgba(0,0,0,.22)}
.hanger.front{left:110px}
.hanger.back{left:631px}
.abs{position:absolute}
.top-art{position:absolute;left:0;top:0}

/* logo */
.logo{position:absolute;left:150px;top:410px;width:170px;text-align:center;font-family:"Roboto Condensed",sans-serif;font-weight:700;color:var(--ink);font-size:40px;line-height:40px;letter-spacing:1px}

/* front headline band */
.headline-band{position:absolute;left:0;top:517px;width:430px;height:118px;background:var(--red)}
.kicker{position:absolute;left:0;width:459px;text-align:center;font-family:"Montserrat",sans-serif;font-weight:300;color:var(--white)}
.front .kicker{top:528px;font-size:26px}
.front .title{position:absolute;left:0;width:459px;top:560px;text-align:center;font-family:"Montserrat",sans-serif;font-weight:900;color:var(--white);font-size:46px;letter-spacing:-.5px}
.tagline-pill{position:absolute;left:52px;top:620px;width:353px;height:29px;border-radius:15px;background:#ececec;font-size:16px;line-height:29px;text-align:center;color:var(--text)}

.benefit{position:absolute;top:668px;width:86px;text-align:center}
.benefit .badge{width:58px;height:58px;margin:0 auto;border-radius:50%;border:2px dotted var(--red);display:flex;align-items:center;justify-content:center}
.benefit .label{margin-top:14px;font-weight:700;font-size:18px;line-height:17px;color:var(--text)}

.offer-frame{position:absolute;left:27px;top:844px;width:407px;height:150px;border:2px dotted var(--red);border-bottom:none;border-radius:12px 12px 0 0}
.tag{position:absolute;height:30px;background:var(--ink);color:var(--white);font-family:"Montserrat",sans-serif;font-weight:300;text-align:center;clip-path:polygon(8% 0,92% 0,100% 50%,92% 100%,8% 100%,0 50%)}
.front .tag{left:124px;top:829px;width:208px;font-size:21px;line-height:30px}
.big-pct{position:absolute;font-family:"Montserrat",sans-serif;font-weight:900;color:var(--red);letter-spacing:-4px;line-height:1}
.front .big-pct{left:50px;top:866px;font-size:98px}
.off{position:absolute;font-family:"Montserrat",sans-serif;font-weight:900;color:var(--red);line-height:1}
.front .off{left:270px;top:873px;font-size:40px}
.first-call{position:absolute;left:270px;top:910px;font-family:"Montserrat",sans-serif;font-weight:400;font-size:21px;line-height:22px;color:var(--ink)}

/* footer */
.footer{position:absolute;left:0;top:985px;width:459px;height:69px}
.call{position:absolute;left:44px;top:13px;color:var(--white);border-left:1px solid rgba(255,255,255,.8);padding-left:5px}
.call small{display:block;font-family:"Montserrat",sans-serif;font-weight:300;font-size:13px;line-height:14px}
.call strong{display:block;font-family:"Montserrat",sans-serif;font-weight:900;font-size:17px;line-height:24px;white-space:nowrap}
.web{position:absolute;left:266px;top:18px;color:var(--white);border-left:1px solid rgba(255,255,255,.6);padding-left:6px;font-family:"Montserrat",sans-serif;font-weight:400;font-size:12px;line-height:16px;white-space:nowrap}
.web b{font-weight:700}

/* back */
.back .kicker{left:31px;width:auto;top:290px;text-align:left;font-size:24px}
.issue-title{position:absolute;left:31px;font-family:"Montserrat",sans-serif;font-weight:900;color:var(--white);line-height:1;letter-spacing:-.5px}
.intro{position:absolute;left:31px;top:464px;width:250px;font-size:17px;line-height:20px;color:var(--white)}
.service{position:absolute;font-weight:700;font-size:17px;line-height:20px;color:var(--text);padding-left:15px}
.bolt-mark{position:absolute;left:0;top:2px;width:10px;height:16px}
.why-frame{position:absolute;left:43px;top:723px;width:373px;height:134px;border:2px dotted var(--red);border-radius:12px}
.back .tag{left:125px;top:709px;width:210px;font-size:20px;line-height:30px}
.mascot{position:absolute;left:58px;top:740px;width:118px;height:115px;border-radius:8px;background:linear-gradient(160deg,#e33a3a 0%,#d94141 45%,#3f66b0 100%)}
.reason{position:absolute;left:201px;font-size:16px;line-height:18px;color:var(--text);padding-left:16px}
.book-bar{position:absolute;left:71px;top:858px;width:317px;height:29px;background:var(--charcoal);border-radius:0 0 14px 14px;color:var(--white);font-size:12px;line-height:29px;text-align:center;letter-spacing:.3px}
.back .big-pct{left:38px;top:890px;font-size:92px}
.back .off{left:240px;top:893px;font-size:36px}
.fine{position:absolute;left:245px;top:927px;font-style:italic;font-size:9px;line-height:11px;color:var(--ink)}
.social-strip{position:absolute;left:270px;top:958px;width:189px;height:26px;background:var(--red);clip-path:polygon(4% 0,100% 0,100% 100%,0 100%);color:var(--white)}
.social-strip .follow{position:absolute;left:10px;top:5px;font-weight:700;font-size:6px;line-height:8px;white-space:nowrap}
.social-strip .names{position:absolute;left:110px;top:4px;font-weight:700;font-size:7px;line-height:9px;border-left:1px solid rgba(255,255,255,.7);padding-left:4px;white-space:nowrap}
</style>
</head>
<body>

<!-- FRONT SIDE -->
<section class="hanger front">
  <svg class="top-art" width="459" height="517" viewBox="0 0 459 517">
    <defs>
      <linearGradient id="frontPhoto" x1="0" y1="0" x2="1" y2="1">
        <stop offset="0" stop-color="#6d6f73"/>
        <stop offset=".55" stop-color="#bdbdbd"/>
        <stop offset="1" stop-color="#8a8a8a"/>
      </linearGradient>
      <linearGradient id="frontRed" x1="0" y1="0" x2="0" y2="1">
        <stop offset="0" stop-color="#e31b1b"/>
        <stop offset="1" stop-color="#f03a3a"/>
      </linearGradient>
    </defs>
    <rect width="459" height="517" fill="#ffffff"/>
    <g role="img" aria-label="Photo of an electrician in a hard hat drilling into a wall panel">
      <polygon points="170,0 459,0 459,517 0,517 0,475 180,200" fill="url(#frontPhoto)"/>
    </g>
    <g role="img" aria-label="Red-tinted photo of an open electrical panel">
      <polygon points="0,0 285,0 287,28 190,150 230,150 30,430 95,142 0,142" fill="url(#frontRed)"/>
    </g>
    <polygon points="459,330 459,517 340,517" fill="#1d1d1d"/>
    <circle cx="229" cy="140" r="62" fill="#e3e3e3"/>
  </svg>

  <div class="logo">K&amp;T<br>Electric</div>

  <div class="headline-band"></div>
  <svg class="abs" style="left:0;top:517px" width="459" height="212" viewBox="0 0 459 212">
    <polygon points="430,0 459,0 459,25 405,212 400,212" fill="#1d1d1d"/>
  </svg>
  <p class="kicker">NEED A RELIABLE</p>
  <h1 class="title">ELECTRICIAN?</h1>
  <p class="tagline-pill">Your Local Electrical Expert is Just Around the Corner!</p>

  <div class="benefit" style="left:32px">
    <div class="badge"><svg width="30" height="30" viewBox="0 0 30 30" fill="none" stroke="#555" stroke-width="1.5"><circle cx="15" cy="15" r="11"/><path d="M15 8v7l5 3"/></svg></div>
    <p class="label">Quick<br>Response<br>Times</p>
  </div>
  <div class="benefit" style="left:126px">
    <div class="badge"><svg width="30" height="30" viewBox="0 0 30 30" fill="none" stroke="#555" stroke-width="1.5"><circle cx="15" cy="15" r="11"/><path d="M18 10h-4a2.5 2.5 0 0 0 0 5h2a2.5 2.5 0 0 1 0 5h-5M15 7v16"/></svg></div>
    <p class="label">Affordable<br>Rates</p>
  </div>
  <div class="benefit" style="left:221px">
    <div class="badge"><svg width="30" height="30" viewBox="0 0 30 30" fill="none" stroke="#555" stroke-width="1.5"><path d="M6 14a9 9 0 0 1 18 0zM4 14h22M9 24h12"/></svg></div>
    <p class="label">Quality<br>Workman-<br>ship</p>
  </div>
  <div class="benefit" style="left:317px">
    <div class="badge"><svg width="30" height="30" viewBox="0 0 30 30" fill="none" stroke="#555" stroke-width="1.5"><rect x="7" y="5" width="16" height="20" rx="1"/><path d="M11 15l3 3 6-6"/></svg></div>
    <p class="label">Fully<br>Licensed<br>&amp; Insured</p>
  </div>

  <div class="offer-frame"></div>
  <p class="tag">SPECIAL OFFER:</p>
  <p class="big-pct">10%</p>
  <p class="off">OFF</p>
  <p class="first-call">YOUR FIRST<br>SERVICE CALL!</p>

  <div class="footer">
    <svg class="abs" style="left:0;top:0" width="459" height="69" viewBox="0 0 459 69">
      <rect width="459" height="69" fill="#333333"/>
      <polygon points="0,0 224,0 210,69 0,69" fill="#ee1c1c"/>
      <polygon points="240,-30 205,35 222,35 204,69 250,20 234,20 248,-30" fill="#c9c9cc"/>
      <circle cx="253" cy="37" r="7" fill="none" stroke="#ee1c1c" stroke-width="2"/>
      <path d="M246 37h14M253 30v14" stroke="#ee1c1c" stroke-width="1.5"/>
      <path d="M18 28q-3 10 7 20l3-3-4-5-3 2q-3-5-1-9l3-1-1-6z" fill="#fff"/>
    </svg>
    <p class="call"><small>Call Us Today:</small><strong>(555) 318-4702</strong></p>
    <p class="web">Visit Our Website<br>www.<b>kandtelectric</b>.example</p>
  </div>
</section>

<!-- BACK SIDE -->
<section class="hanger back">
  <svg class="top-art" width="459" height="561" viewBox="0 0 459 561">
    <defs>
      <linearGradient id="backPanel" x1="0" y1="0" x2="0" y2="1">
        <stop offset="0" stop-color="#e01616"/>
        <stop offset="1" stop-color="#f23a3a"/>
      </linearGradient>
      <linearGradient id="backPhoto" x1="0" y1="0" x2="1" y2="1">
        <stop offset="0" stop-color="#d9d9d9"/>
        <stop offset=".6" stop-color="#8d9098"/>
        <stop offset="1" stop-color="#5e6168"/>
      </linearGradient>
    </defs>
    <rect width="459" height="561" fill="#ffffff"/>
    <g role="img" aria-label="Red-tinted photo of wired electrical breaker panels">
      <polygon points="0,0 338,0 160,280 330,280 265,561 0,561" fill="url(#backPanel)"/>
    </g>
    <g role="img" aria-label="Photo of an electrician in a hard hat using a tablet at a panel">
      <polygon points="340,0 459,0 459,260 370,330 300,470 330,290 165,280" fill="url(#backPhoto)"/>
    </g>
    <polygon points="405,0 459,0 459,140 370,140" fill="#1d1d1d"/>
    <polygon points="459,260 459,300 300,470 320,360" fill="#9a9ca3"/>
    <circle cx="229" cy="140" r="62" fill="#e3e3e3"/>
    <circle cx="343" cy="418" r="82" fill="#ffffff"/>
    <circle cx="343" cy="418" r="78" fill="#8b8f6e" role="img" aria-label="Photo of hands testing an outlet with a multimeter"/>
  </svg>

  <p class="kicker">DON’T LET</p>
  <p class="issue-title" style="top:312px;font-size:42px">ELECTRICAL</p>
  <p class="issue-title" style="top:345px;font-size:60px">ISSUES</p>
  <p class="issue-title" style="top:400px;font-size:33px">KEEP YOU IN</p>
  <p class="issue-title" style="top:432px;font-size:33px">THE DARK!</p>
  <p class="intro">From flickering lights to complete system upgrades, we’ve got all your residential electrical needs covered. Our services include:</p>

  <p class="service" style="left:31px;top:576px"><svg class="bolt-mark" viewBox="0 0 10 16"><path d="M7 0L1 9h4l-2 7 6-9H5z" fill="#ee1c1c"/></svg>Electrical<br>Repairs &amp;<br>Troubleshooting</p>
  <p class="service" style="left:176px;top:576px"><svg class="bolt-mark" viewBox="0 0 10 16"><path d="M7 0L1 9h4l-2 7 6-9H5z" fill="#ee1c1c"/></svg>Lighting<br>Installation<br>&amp; Upgrades</p>
  <p class="service" style="left:287px;top:576px"><svg class="bolt-mark" viewBox="0 0 10 16"><path d="M7 0L1 9h4l-2 7 6-9H5z" fill="#ee1c1c"/></svg>Safety Inspections<br>&amp; Code Compliance</p>
  <p class="service" style="left:31px;top:655px"><svg class="bolt-mark" viewBox="0 0 10 16"><path d="M7 0L1 9h4l-2 7 6-9H5z" fill="#ee1c1c"/></svg>Energy-Efficient<br>Solutions</p>
  <p class="service" style="left:176px;top:654px"><svg class="bolt-mark" viewBox="0 0 10 16"><path d="M7 0L1 9h4l-2 7 6-9H5z" fill="#ee1c1c"/></svg>24/7 Emergency<br>Services</p>

  <div class="why-frame"></div>
  <div class="mascot" role="img" aria-label="Cartoon electrician mascot holding a lightning bolt"></div>
  <p class="tag">WHY CHOOSE US?</p>
  <p class="reason" style="top:747px"><svg class="bolt-mark" viewBox="0 0 10 16"><path d="M7 0L1 9h4l-2 7 6-9H5z" fill="#ee1c1c"/></svg>Friendly, Local Service</p>
  <p class="reason" style="top:773px"><svg class="bolt-mark" viewBox="0 0 10 16"><path d="M7 0L1 9h4l-2 7 6-9H5z" fill="#ee1c1c"/></svg>Over 30 Years of Experience</p>
  <p class="reason" style="top:799px"><svg class="bolt-mark" viewBox="0 0 10 16"><path d="M7 0L1 9h4l-2 7 6-9H5z" fill="#ee1c1c"/></svg>Satisfaction Guaranteed</p>
  <p class="reason" style="top:825px"><svg class="bolt-mark" viewBox="0 0 10 16"><path d="M7 0L1 9h4l-2 7 6-9H5z" fill="#ee1c1c"/></svg>Upfront Pricing</p>

  <p class="book-bar">BOOK YOUR APPOINTMENT NOW AND CLAIM YOUR</p>
  <p class="big-pct">10%</p>
  <p class="off">OFF</p>
  <p class="fine">Offer valid for new customers on the first visit only.<br>Mention this door hanger when booking.</p>

  <div class="social-strip">
    <p class="follow">Follow Us on Social Media<br>for More Tips and Special Offers!</p>
    <p class="names">Chatterpage · Pixmosaic<br>Linkline · Quibbler</p>
  </div>

  <div class="footer">
    <svg class="abs" style="left:0;top:0" width="459" height="69" viewBox="0 0 459 69">
      <rect width="459" height="69" fill="#333333"/>
      <polygon points="0,0 224,0 210,69 0,69" fill="#ee1c1c"/>
      <polygon points="240,-30 205,35 222,35 204,69 250,20 234,20 248,-30" fill="#c9c9cc"/>
      <circle cx="253" cy="37" r="7" fill="none" stroke="#ee1c1c" stroke-width="2"/>
      <path d="M246 37h14M253 30v14" stroke="#ee1c1c" stroke-width="1.5"/>
      <path d="M18 28q-3 10 7 20l3-3-4-5-3 2q-3-5-1-9l3-1-1-6z" fill="#fff"/>
    </svg>
    <p class="call"><small>Call Us Today:</small><strong>(555) 318-4702</strong></p>
    <p class="web">Visit Our Website<br>www.<b>kandtelectric</b>.example</p>
  </div>
</section>

</body>
</html>
```